MENU DESIGN FOR KESARI LOOM RESTUARNT

1.NEED TRI FOLD MENU FOR TAKE OUT FRONT AND BACK JUST LIKE I HAVE ATTACHED THE MENU .....IT COULD EVEN ALMOST IDENTICAL. ( COPY THE MENU ITEMS AT THE BOTTOM OF THIS PAGE.

2. I NEED A POSTER FOR LUNCH COMBO 11AM-2PM
THRE ARE 3 COMBOS
A....HIT_____ SERVED WITH RICE AND ONE ENTREE WITH PCS OF FRESH TANDOORI NAAN BREAD IN 7" CONTAINER....13

B...SUPERHIT......SERVED WITH RICE, SALAD.NAAN, POP, AND ONE ENTREE .....$15

C...BLOCKBUSTER.....SERVED WITH RICE, SALAD, NAAN, POP, AND ONE ENTEE AND ONE ADD-ON....$18

BOTTOM OF THE PAGE PLEASE WE WILL HAVE LIST OF ENTEE + ADD WITH PRICE ...PLS NOTE WE WILL HAVE 10 ENTREE WHIS WILL ALSO TRANSLATE TO 10 ADD ON

AFTER THE DESIGN YOU CAN ATTACH THIS POSTER TO TAKEOUNT MENU WHICH WILL TAKE 1 PAGE.

HER IS THE TAKE OUT MENU ITEMS IN SECTIONS

TANDOORI DINNERS for meat lovers….
Served with rice, salad, roti or naan.

"Signature" BONELESS CHICKEN TIKKA ……………………………
-appetizer $10 / single dinner $15/ big dinner $20
boneless diced chicken marinated with KL secret masala and cooked in tandoor.

"Haryali" BONELESS CHICKEN TIKKA ……………………………………
10/15/20
boneless dice chicken marinated with mint and cilantro cooked in tandoor

"Malai" BONELESS CHICKEN TIKKA…………………………………………………………………
10/15/20
boneless diced chicken marinated with cheese, yogurt and mild spices and cooked in tandoor

"Hot n Spicy" BONELESS CHICKEN TIKKA……………………………………………………………………….
12/17/25
boneless dice chicken marinated with hot spices and cooked in tandoor.

CHICKEN SEEKH KABOB…………………………………………………………………10/15/20

minced ground chicken cooked in tandoor

TANDOORI CHICKEN bone-in……………………………………………………………………………10/15/20
chicken pcs marinated in seasoning and cooked in tandoor.……………………

TANDOORI CHICKEN LEGS

8/10/18

marinated chicken legs cooked in tandoor

TANDOORI CHICKEN WINGS

8/10/18

marinated chicken wings cooked in the tandoor

LAMB CHOPS KABOB……………………………………………………………………

18/22/32

marinated lamb chops in blended spices cooked in tandoor.

SHOULDER LAMB CHOP KEBOB

15/20/30

FISH TIKKA ………………………………………………………………………………………………15/20/32

Moist & tender spice marinated chunks of Salmon cooke in tandoor

TANDOOR SHRIMP………………………………………………………………

17/20/35

marinated shrimp cooked in tandoor.

TANDOORI PANEER TIKKA

10/15/20

chanks of paneer marinated in spices cooked in a tandoor

TANDOORI VEG. KEBOBS

10/15/20

marinated fresh vegetables cooked in a tandoor

**********+++++++=====

—————————TANDOORI KEBOB PLATERS————————————————

4 PERSON $32 6 PERSON $42 8 PERSON $50

———————————TANDOORI WRAPS———————————————————

CHICKEN TIKKA KEBOB WRAP $10
CHICKEN SEEKH KEBOB WRAPS $10
“HOT & SPICY” CHICKEN TIKKA WRAP $12
SALMON FISH TIKKA WRAP
PANEER TIKKA WRAP

VEGETARIAN MAIN COURSE CURRIES SMALL MEDIUM LARGE

CHANNA MASALA $6 $10 $15

DAAL MAKHANI 8 12 17

PANEER MAKHANI 8 12 17

KARAHI PANEER 8 12 17

PALAK PANEER 8 12 17

CHILLIE PANEER 9 13 18

BENGAN AFGHANI 9 12 17

BENGAN BHARTHA 8 12 17

MIX VEG. 8 12 17

VEG. MANCHURIAN 10 14 18

==========SIDES========
TAWA ROTI $1.50
TANDOORI ROTI $1.75
TANDOORI BUTTER NAAN $2
TANDOORI PLAIN NAAN $1.75
TANDOORI GARLIC NAAN $2.50
PLAIN PARATHA $2.50
TAWA NAAN $3.00
BATURA $1.50

BASMATI RICE SMALL $3.50SM LARGE $5
SALAD $3.50
SALAD UPGRADE $4.75
MASALA FRIES
RAITA $3.50

=============== PLATER / ROLL 12PM-4PM =============

2 VEG. CURRY+NAAN+RICE $10
1 VEG. CURRY+NAAN+RICE $8.50
VEG. CURRY ON RICE $7.50

CHANNA / KADAI PANEER / PALAK PANEER / PALAK PANEER / MIX VEG. $8

MEAT LOVERS MAIN COURSE CURRIES

BONELESS BUTTER CHICKEN……………………………………………………………
S $11 ……M15…….L24
diced boneless tandoori chicken cooked in butter and creamy sauce.

KADAI CHICKEN MASALA…………………………………………………………………
S$11……..M$15……..L24
boneless chicken cooked in spices and thick gravy.

CHICKEN TIKKA MASALA………………………………………………………………………………11/15/24
tandoori chicken tikka cooked with spice and gravy.

CHICKEN KOFTA CURRY………………………………………………………………………………11/15/24
chicken kofta cooked in tomatoes and spices.

AFGHANI CHICKEN HARYALI…………………………………………………………………………………11/15/24
chicken cooked with spinach and spices.

CHICKEN VINDALOO……………………………………………………………………………
12/18/29
boneless chicken cooked with potatoes & spices in a thick gravy.

CHICKEN CURRY…..

11/15/24

boneless chicken cooked in the soup gravy

CHILLIE CHICKEN WITHG RAVY

12/18/29

METHI MALAI CHICKEN

11/15/24

boneless chicken cooked cheese and methi

LAMB VINDALOO……………………………………………………………………

13/20/29

boneless lamb cooked with potatoes & spices in a thick gravy.

AFGHANI HARYALI LAMB………………………………………………………………………
13/20/29
lamb cooked with spinach and spices.

SHRIMP VINDALOO……………………………………………………………………
13/20/29
shrimp cooked in the thick spicy sauce.

TANDOORI SHRIMP MASALA

15/25/32

FISH TIKKA MASALA…………………………………………………………………………

15/20/32

fish in spicy curry sauce.

SPECIAL MEALS

LAMB BIRYANI……………………………………………………………………………………………………………..$10

lamb seasoned with fragrant spices and fresh herbs.

CHICKEN BIRYANI…………………………………………………………………………………………………………$9
chicken seasoned with fragrant spices and fresh herbs cooked with rice.

check out our website www.kesariloom.ca FOR

SPCIALS DAILY
SPECIAL ORDERS MENU
DESSRT MENU
DRINK MENU
DESSERT MENU

BENGAN BHARTA
comprises bhurtha (minced vegetables) made from eggplant (baingan) which is grilled over charcoal or direct fire, to infuse the dish with a smoky flavour

PANEER MAKHANI
COTTAGE CHEESE COOKED WITH BUTTER AND CREAMY SAUCE.

VEG. MANCHURIAN AND CHILLIE PANEER- PLS KEEP AT THE SAME PLACE

PLS KEEP VEG SNACKS WITH PRICE CHANGE

ALL VEG SAME WITH PRICE

Target Market(s)

PEOPLE WHO LOVE FRESH INDIAN FOOD

Font styles to use
Decorative
Script

Colors
ec1f27
fdf1e7
f68e4e
fbed22
ffcf3e
faa54b
f68d4c
e34197

Requirements
Must have
• LOGO
• SIZES
• PRICE
• SOME VISUAL
• FILM OR MOVIE THEME
• ACTOR DIRECTOR CINEMA FEEL
Nice to have
• CURRY COMBOS IN FILM REEL NICE TO HAVE BUT NOT A MUS AS I M LOOKING FOR MORE ELEGANT DESIGN NOT A CARTOONI OR BUSY
• MUST BE PROFESSIONAL LOOK
• SIMPLE
• EASY
• ATTRACTIVE

```html
<!DOCTYPE html>
<html lang="en">
<head>
<meta charset="utf-8">
<title>Kesari Loom – Lunch Combos</title>
<link rel="stylesheet" href="https://fonts.googleapis.com/css2?family=Rye&family=Ultra&family=Roboto+Condensed:wght@400;700&display=swap">
<style>
  :root{
    --burlap:#c9b184;
    --burlap-dark:#b59a6a;
    --board:#1f1f1f;
    --lime:#8cc63f;
    --ink:#1a1a1a;
    --white:#ffffff;
    --muted:#bdbdbd;
  }
  *{box-sizing:border-box;margin:0;padding:0}
  html,body{width:807px;height:1200px;overflow:hidden}
  body{font-family:"Roboto Condensed",Arial,sans-serif;background:var(--burlap)}
  .poster{position:relative;width:807px;height:1200px;overflow:hidden}
  .backdrop{position:absolute;inset:0;background:radial-gradient(ellipse at center,var(--burlap) 55%,var(--burlap-dark) 100%)}
  .board{position:absolute;left:48px;top:32px;width:711px;height:1125px;background:var(--board)}

  .header{position:absolute;left:0;right:0;top:14px;height:80px}
  .chef-mark{position:absolute;left:262px;top:6px;width:56px;height:68px;border-radius:10px;background:linear-gradient(#ffffff,#d9d9d9)}
  .title{position:absolute;left:330px;top:0;font-family:"Rye",serif;font-size:40px;line-height:1;color:var(--white);letter-spacing:2px}
  .subtitle{position:absolute;left:332px;top:44px;font-size:13px;letter-spacing:3px;color:var(--white)}
  .hours{position:absolute;left:356px;top:64px;font-size:13px;letter-spacing:3px;color:var(--white)}

  .stripes{position:absolute;height:56px;background:repeating-linear-gradient(to bottom,var(--lime) 0 6px,transparent 6px 14px)}

  .combo{position:absolute;background:var(--lime);border:9px dotted var(--white);border-radius:18px;text-align:center;color:var(--ink);padding-top:14px}
  .combo-name{font-family:"Ultra",serif;font-size:46px;line-height:.95;color:var(--white);-webkit-text-stroke:2px var(--ink);text-transform:uppercase}
  .combo-desc{font-size:10px;line-height:1.35;margin:6px auto 0;width:150px;text-transform:uppercase;letter-spacing:.5px}
  .combo-price{font-family:"Ultra",serif;font-size:34px;line-height:1;color:var(--white);-webkit-text-stroke:1.5px var(--ink);margin-top:10px}
  .combo--hit{left:100px;top:100px;width:256px;height:190px}
  .combo--super{left:396px;top:282px;width:220px;height:200px;padding-top:12px}
  .combo--super .combo-name{font-size:36px}
  .combo--block{left:100px;top:410px;width:256px;height:210px;padding-top:12px}
  .combo--block .combo-name{font-size:34px}

  .list-card{position:absolute;top:648px;height:326px;background:var(--lime);border-radius:16px;padding:14px 18px;color:var(--ink)}
  .list-card h2{font-family:"Rye",serif;font-size:32px;line-height:1.1;text-align:center;font-weight:400;margin-bottom:8px}
  .list-card--entree{left:27px;width:323px}
  .list-card--addon{left:361px;width:323px}
  .group-title{font-family:"Rye",serif;font-size:15px;text-align:center;margin-top:4px}
  .entree-list{list-style:none;text-align:center;font-size:12px;line-height:1.35;text-transform:lowercase}
  .addon-list{list-style:none;font-size:12px;line-height:1.5}
  .addon-list li{display:flex;justify-content:space-between}
  .addon-note{font-size:11px;margin-top:6px}

  .footnotes{position:absolute;top:982px;left:0;right:0;display:flex;justify-content:space-around;font-size:11px;color:var(--muted)}

  .footer{position:absolute;top:1010px;left:27px;right:27px;height:64px;display:flex;align-items:center;justify-content:space-between;color:var(--white)}
  .brand{display:flex;align-items:center;gap:8px;font-family:"Rye",serif;font-size:18px;color:var(--lime)}
  .brand-dot{width:14px;height:14px;background:var(--lime)}
  .service{text-align:center;font-size:10px;letter-spacing:2px}
  .service .phone{display:block;font-size:13px;font-weight:700;color:var(--lime);margin-top:4px;letter-spacing:1px}
  .contact{font-size:11px;text-align:center;line-height:1.4;width:160px}
  .address{position:absolute;top:1088px;left:0;right:0;text-align:center;font-size:10px;color:var(--muted);letter-spacing:.5px}
</style>
</head>
<body>
<div class="poster">
  <div class="backdrop" role="img" aria-label="Woven burlap texture background"></div>
  <div class="board">
    <header class="header">
      <div class="chef-mark" role="img" aria-label="Chef hat and moustache illustration"></div>
      <h1 class="title">LUNCH</h1>
      <p class="subtitle">VEGETARIAN LOVERS</p>
      <p class="hours">11AM - 2PM ONLY</p>
    </header>

    <div class="stripes" style="left:0;top:150px;width:120px"></div>
    <div class="stripes" style="left:330px;top:180px;width:381px"></div>
    <div class="stripes" style="left:580px;top:260px;width:131px"></div>
    <div class="stripes" style="left:0;top:470px;width:120px"></div>
    <div class="stripes" style="left:330px;top:520px;width:381px"></div>

    <section class="combo combo--hit">
      <h2 class="combo-name">Hit</h2>
      <p class="combo-desc">Rice and one entree with fresh tandoori naan</p>
      <p class="combo-price">$13</p>
    </section>
    <section class="combo combo--super">
      <h2 class="combo-name">Super<br>Hit</h2>
      <p class="combo-desc">One entree with rice, salad, naan &amp; pop</p>
      <p class="combo-price">$15</p>
    </section>
    <section class="combo combo--block">
      <h2 class="combo-name">Block<br>Buster</h2>
      <p class="combo-desc">One entree, one add on with rice, salad, naan &amp; pop</p>
      <p class="combo-price">$18</p>
    </section>

    <section class="list-card list-card--entree">
      <h2>ENTRÉ</h2>
      <h3 class="group-title">CURRIES</h3>
      <ul class="entree-list">
        <li>bengan afghani</li><li>palak paneer</li><li>aloo gobi</li><li>daal makhani</li><li>kadai paneer</li>
      </ul>
      <h3 class="group-title">TANDOORI</h3>
      <ul class="entree-list">
        <li>paneer makhani</li><li>mutter paneer</li><li>channa masala</li><li>mix veg</li><li>bengan bhartha</li><li>paneer tikka</li>
      </ul>
    </section>

    <section class="list-card list-card--addon">
      <h2>ADD ON</h2>
      <ul class="addon-list">
        <li><span>veg. pakora ( 4 pcs )</span><span>$3</span></li>
        <li><span>aloo tikki ( 2 pcs )</span><span>$3</span></li>
        <li><span>paneer pakora ( 4 pcs )</span><span>$3</span></li>
        <li><span>onion bhaji ( 4 pcs )</span><span>$3</span></li>
        <li><span>samosa ( 2 pcs )</span><span>$3</span></li>
        <li><span>masala fries</span><span>$3</span></li>
        <li><span>veg. curry</span><span>$3</span></li>
        <li><span>raita</span><span>$3</span></li>
        <li><span>naan</span><span>$2</span></li>
        <li><span>roti</span><span>$2</span></li>
        <li><span>rice</span><span>$3</span></li>
        <li><span>salad</span><span>$3</span></li>
      </ul>
      <p class="addon-note">Choose from our fresh daily menu</p>
    </section>

    <div class="footnotes">
      <span>*one entré is subject to availability</span>
      <span>*add on portions are smaller than entré</span>
    </div>

    <footer class="footer">
      <div class="brand"><span class="brand-dot"></span>KESARI LOOM</div>
      <div class="service">DINE IN · TAKEOUT · CATERING<span class="phone">905 555 0182</span></div>
      <p class="contact">Please contact us for Curbside Delivery And Catering</p>
    </footer>
    <p class="address">ADDRESS: 1200 Harbour Road, Unit 4, Milton ON L0P 1A0 · Harbour Rd &amp; Elm St · www.kesariloom.ca</p>
  </div>
</div>
</body>
</html>
```